Podiatry clinic requires a modern revamp and editing of existing website.

I would like a fresh new look and updated information for my current business website. An easy to navigate site with prominent address and phone number for call to action. We are a podiatry clinic that focuses on general and sports podiatry.
I would like 4 pages; including Home page, About Us, Services & Contact.
www.brambleridgefootcare.com

Target Market(s)

Active working professionals.

Industry/Entity Type

Medical

Coding

Coded - Design and coding required

Number of Pages Required

4 page

Font styles to use
Sans Serif

Colors
6b449b

Requirements
Must have
• A modern look with logo and active images; clean and uncluttered. Visible phone number and address for call to action.
• 4 pages - Home, About Us, Services, Contact.
• Home page - update address & service logos.
• About Us - update of personal information.
• Services - Revamp of existing page.
• Contact page to include Google map, email & phone number.
Nice to have
• Ability to add content easily; eg. a blog or adding video onto Home page.
• Link to Facebook page.

```html
<!DOCTYPE html>
<html lang="en">
<head>
<meta charset="utf-8">
<title>Bramble Ridge Foot Care</title>
<link rel="stylesheet" href="https://fonts.googleapis.com/css2?family=Open+Sans:ital,wght@0,400;0,600;0,700;1,400&family=Playfair+Display:wght@400;700&family=Play:wght@700&display=swap">
<style>
:root{
  --purple:#6b449b;
  --purple-dark:#5b3889;
  --ink:#333;
  --muted:#666;
  --soft:#999;
  --line:#e2e2e2;
  --band:#f4f4f4;
  --footer-base:#2b2b2b;
  --white:#fff;
  --accent:#3a9ad9;
}
*{box-sizing:border-box;margin:0;padding:0}
html,body{width:1200px;height:2182px;overflow:hidden}
body{position:relative;background:var(--white);font-family:"Open Sans",Arial,sans-serif;color:var(--ink)}
.abs{position:absolute}

/* top bar */
.topbar{top:0;left:0;width:1200px;height:65px;background:var(--white)}
.top-info{display:flex;align-items:center;gap:14px;font-size:11px;color:var(--muted);line-height:1.4}
.top-info strong{display:block;color:var(--ink);font-size:12px;font-weight:700}
.top-call{left:90px;top:15px}
.top-hours{left:966px;top:18px}
.brand{left:500px;top:10px;display:flex;align-items:center;gap:10px}
.brand-mark{width:40px;height:40px;border-radius:50%;background:var(--purple)}
.brand-name{font-family:"Open Sans",Arial,sans-serif;font-weight:700;font-size:21px;color:var(--purple);letter-spacing:.5px}

/* navigation */
.nav{top:65px;left:0;width:1200px;height:65px;background:var(--band);display:flex;justify-content:center;align-items:center;gap:8px}
.nav a{font-size:12px;color:var(--muted);text-decoration:none;padding:9px 13px;text-transform:uppercase}
.nav a.active{background:var(--purple);color:var(--white)}

/* hero */
.hero-photo{top:130px;left:0;width:1200px;height:523px;background:linear-gradient(180deg,#bfb98a 0%,#d9cf9a 25%,#9c8c52 55%,#6e5a2c 80%,#4a3b1f 100%)}
.hero-title{left:44px;top:268px;font-family:"Play",Arial,sans-serif;font-weight:700;font-size:41px;line-height:53px;color:var(--purple);text-align:center}
.appointment{left:803px;top:195px;width:340px;height:423px;background:var(--purple);border-radius:14px;padding:26px 24px}
.appointment h2{font-family:"Playfair Display",Georgia,serif;font-size:21px;font-weight:700;color:var(--white);margin-bottom:20px}
.field{display:block;width:292px;height:41px;background:var(--white);border:1px solid #ddd;font-size:12px;color:#888;padding:12px 12px;margin-bottom:11px}
.field.message{height:106px}
.send{display:inline-block;width:125px;height:35px;background:#eee;color:var(--ink);font-size:12px;line-height:35px;text-align:center;margin-top:4px}

/* about */
.hours-card{left:66px;top:753px;width:339px;height:367px;border:10px solid #ececec;padding:28px 28px}
.card-head{font-size:13px;font-weight:700;color:var(--ink);display:flex;align-items:center;gap:6px;margin-bottom:14px}
.hours-row{display:flex;justify-content:space-between;font-size:12px;color:var(--muted);padding:8px 0;border-bottom:1px solid var(--line)}
.hours-row:last-of-type{border-bottom:none}
.help-text{font-size:11.5px;color:var(--muted);text-transform:uppercase;line-height:20px;margin-bottom:14px}
.btn-solid{display:inline-block;background:var(--purple);color:var(--white);font-size:12px;padding:8px 22px}
.about{left:434px;top:762px;width:706px}
.about-kicker{font-family:"Playfair Display",Georgia,serif;font-size:24px;color:#aaa;font-weight:700}
.about h1{font-family:"Playfair Display",Georgia,serif;font-size:36px;color:var(--muted);font-weight:700;margin:0 0 14px}
.about p{font-size:12px;line-height:20px;color:var(--muted);margin-bottom:14px}
.about p.lead{font-style:italic}
.btn-ghost{display:inline-block;border:1px solid #ccc;border-radius:2px;font-size:13px;color:var(--ink);padding:9px 24px;background:var(--white)}

/* services */
.services-title{top:1192px;left:0;width:1200px;text-align:center;font-family:"Playfair Display",Georgia,serif;font-weight:700;font-size:28px;color:var(--ink)}
.service{top:1259px;width:337px;height:322px;border:2px solid #e8e8e8;text-align:center;padding:28px 36px}
.service-icon{width:82px;height:82px;border:2px solid #e0e0e0;border-radius:50%;margin:0 auto 26px;display:flex;align-items:center;justify-content:center}
.service h3{font-size:14px;font-weight:600;color:var(--ink);margin-bottom:10px}
.service p{font-size:12px;line-height:21px;color:#888;margin-bottom:18px}
.service .btn-ghost{font-size:12px;padding:7px 20px}

/* partners */
.partners{top:1597px;left:0;width:1200px;height:177px;background:var(--band)}
.partner{top:1638px;width:247px;height:94px;background:var(--white)}

/* footer */
.footer{top:1774px;left:0;width:1200px;height:321px;background:var(--purple);color:var(--white)}
.footer-col{top:1774px;height:321px}
.footer-divider{top:1774px;width:1px;height:321px;background:var(--purple-dark)}
.footer h4{font-size:13px;font-weight:700;text-transform:uppercase;margin-bottom:24px}
.footer-list{font-size:12px;line-height:31px}
.footer-brand{left:328px;top:1838px;width:551px;text-align:center}
.footer-brand .brand-name{color:var(--white);font-size:34px}
.footer-brand p{font-size:12px;line-height:20px;margin:26px 40px 0}
.footer-rule{left:400px;top:2064px;width:408px;border-top:1px dashed rgba(255,255,255,.35)}
.contact{right:60px;top:1888px;text-align:right;font-size:12px;line-height:20px}
.contact p{margin-bottom:11px}
.socials{display:flex;gap:7px;justify-content:flex-end}
.socials span{width:27px;height:27px;border-radius:50%;background:rgba(255,255,255,.85)}

/* base bar */
.basebar{top:2095px;left:0;width:1200px;height:87px;background:var(--footer-base);color:var(--white);font-size:11px}
.copyright{left:66px;top:2132px;font-size:11px;color:var(--white)}
.base-links{right:92px;top:2132px;font-size:11px;color:var(--white);word-spacing:4px}
.to-top{right:0;top:2117px;width:44px;height:44px;display:flex;align-items:center;justify-content:center}
</style>
</head>
<body>

<header class="abs topbar"></header>
<div class="abs top-info top-call">
  <svg width="16" height="28" viewBox="0 0 16 28" aria-hidden="true"><rect x="1" y="1" width="14" height="26" rx="3" fill="var(--purple)"/><rect x="3.5" y="5" width="9" height="15" fill="#fff"/><circle cx="8" cy="23.5" r="1.6" fill="#fff"/></svg>
  <div>CALL US TODAY!<strong>+(012) 555 0147</strong></div>
</div>
<div class="abs brand"><span class="brand-mark"></span><span class="brand-name">BRAMBLE RIDGE</span></div>
<div class="abs top-info top-hours">
  <svg width="34" height="28" viewBox="0 0 34 28" aria-hidden="true"><path d="M17 2 2 15h4v12h8v-8h6v8h8V15h4z" fill="var(--purple)"/></svg>
  <div>WE ARE OPEN!<strong>Mon-Fri 8:00-16:00</strong></div>
</div>

<nav class="abs nav">
  <a class="active">Home</a><a>About Us</a><a>Services</a><a>Blog</a><a>Contact Us</a>
</nav>

<div class="abs hero-photo" role="img" aria-label="Runner's legs in trail shoes striding across a grassy hilltop at sunrise"></div>
<h2 class="abs hero-title">Welcome to<br>Bramble Ridge Foot Care</h2>

<form class="abs appointment">
  <h2>Make an Appointment</h2>
  <span class="field">Enter Name</span>
  <span class="field">Enter Email</span>
  <span class="field">Appointment Date</span>
  <span class="field message">Enter Message</span>
  <span class="send">Send Message</span>
</form>

<aside class="abs hours-card">
  <div class="card-head"><svg width="12" height="12" viewBox="0 0 12 12" aria-hidden="true"><circle cx="6" cy="6" r="5" fill="none" stroke="var(--purple)" stroke-width="1.5"/><path d="M6 3v3h2" fill="none" stroke="var(--purple)" stroke-width="1.3"/></svg>Opening Hours</div>
  <div class="hours-row"><span>Monday - Friday</span><span>9.00 - 20.00</span></div>
  <div class="hours-row"><span>Saturday</span><span>10.00 - 16.00</span></div>
  <div class="hours-row"><span>Sunday</span><span>9.30 - 18.00</span></div>
  <div class="card-head" style="margin-top:24px"><svg width="13" height="12" viewBox="0 0 13 12" aria-hidden="true"><rect x="1" y="2" width="9" height="9" fill="none" stroke="var(--purple)" stroke-width="1.3"/><path d="M5 7l6-6" stroke="var(--purple)" stroke-width="1.5"/></svg>Need Help?</div>
  <p class="help-text">Just make an appointment to get help from our experts</p>
  <span class="btn-solid">Request an appointment</span>
</aside>

<section class="abs about">
  <div class="about-kicker">About</div>
  <h1>Bramble Ridge Foot Care</h1>
  <p class="lead">Bramble Ridge Foot Care is a Podiatry clinic in the heart of Melbourne CBD. We are located between Ashby &amp; Merton Streets in the Harbourline Business Centre.</p>
  <p>Our podiatrists are fully qualified health professionals who are able to diagnose, treat, manage or help to prevent all medical conditions that affect the feet and lower limb.</p>
  <p>We provide General Podiatry Treatment and some Specialised Services in relation to various foot conditions, including Sports Injuries, Orthotic Therapy and Nail Surgery.</p>
  <span class="btn-ghost">Read more</span>
</section>

<h2 class="abs services-title">SERVICES</h2>

<article class="abs service" style="left:66px">
  <div class="service-icon" role="img" aria-label="Feet icon"><svg width="34" height="40" viewBox="0 0 34 40" aria-hidden="true"><ellipse cx="11" cy="22" rx="7" ry="15" fill="var(--purple)"/><ellipse cx="23" cy="22" rx="7" ry="15" fill="var(--purple)"/></svg></div>
  <h3>Podiatry Treatments</h3>
  <p>Lorem ipsum dolor sit amet, consectetur adipisicing elit. Cum consectetur sit ullam .perspiciatis, deserunt</p>
  <span class="btn-ghost">Read More</span>
</article>
<article class="abs service" style="left:434px">
  <div class="service-icon" role="img" aria-label="Insole icon"><svg width="34" height="40" viewBox="0 0 34 40" aria-hidden="true"><ellipse cx="17" cy="20" rx="8" ry="17" transform="rotate(35 17 20)" fill="var(--purple)"/></svg></div>
  <h3>Podiatry Products Footwear</h3>
  <p>Lorem ipsum dolor sit amet, consectetur adipisicing elit. Cum consectetur sit ullam .perspiciatis, deserunt</p>
  <span class="btn-ghost">Read More</span>
</article>
<article class="abs service" style="left:801px">
  <div class="service-icon"><svg width="40" height="38" viewBox="0 0 40 38" aria-hidden="true"><path d="M20 1l5.6 12.2 13.4 1.4-10 9 2.9 13.2L20 30.1 8.1 36.8 11 23.6 1 14.6l13.4-1.4z" fill="var(--purple)"/></svg></div>
  <h3>Health Wellness Products</h3>
  <p>Lorem ipsum dolor sit amet, consectetur adipisicing elit. Cum consectetur sit ullam .perspiciatis, deserunt</p>
  <span class="btn-ghost">Read More</span>
</article>

<section class="abs partners"></section>
<div class="abs partner" style="left:50px" role="img" aria-label="Partner association badge"></div>
<div class="abs partner" style="left:336px" role="img" aria-label="Partner association badge"></div>
<div class="abs partner" style="left:620px" role="img" aria-label="Claims service badge"></div>
<div class="abs partner" style="left:906px" role="img" aria-label="Health rebate badge"></div>

<footer class="abs footer"></footer>
<div class="abs footer-divider" style="left:328px"></div>
<div class="abs footer-divider" style="left:879px"></div>
<div class="abs footer-col footer" style="left:66px;top:1888px;width:250px;height:auto;background:none">
  <h4>Our Services</h4>
  <div class="footer-list">Podiatry Treatments<br>Podiatry Products Footwear<br>Health Wellness Products</div>
</div>
<div class="abs footer-brand footer" style="height:auto;background:none">
  <div style="display:flex;justify-content:center;align-items:center;gap:14px"><span class="brand-mark" style="width:56px;height:56px;background:var(--white)"></span><span class="brand-name">BRAMBLE RIDGE</span></div>
  <p>Lorem ipsum dolor sit amet, consectetur adipisicing elit. Consequuntur exercitationem repellendus iusto quos, quasi dolorum hic cum voluptatibus, voluptas suscipit numquam quisquam!</p>
</div>
<div class="abs footer-rule"></div>
<div class="abs contact footer" style="left:auto;width:300px;height:auto;background:none">
  <h4>Quick Contact</h4>
  <p>1300 555 214</p>
  <p>info@brambleridgefootcare.com</p>
  <p>Suite 27 / 115 Harlow Street Melbourne<br>3000</p>
  <div class="socials" aria-label="Social links"><span></span><span></span><span></span><span></span><span></span></div>
</div>

<div class="abs basebar"></div>
<div class="abs copyright">Copyright ©2015 Bramble Ridge Foot Care. All Rights Reserved</div>
<div class="abs base-links">Home / Services / About / Contact us /</div>
<div class="abs to-top"><svg width="22" height="14" viewBox="0 0 22 14" aria-hidden="true"><path d="M2 12l9-9 9 9" fill="none" stroke="#fff" stroke-width="2.5"/></svg></div>

</body>
</html>
```